VelmoraTrade.com -Ecommerce Website for Luxury Products

This will be an ecommerce site. A website portal that will allow both consumers to enter one way and see specific purchase options and businesses to enter via a different link that allows B2B to see their specific options once logged into. B2C can purchase both as a guest/or after account is setup. B2B must be approved to set up account. This is front end website project. Back-end integration is separate. Will be hosted on Serventa with a domain registration held at PortaVance. Additional website concept/idea/synergy can be found from sister site-KRWEHospitality.com

```html
<!DOCTYPE html>
<html lang="en">
<head>
<meta charset="UTF-8">
<title>VelmoraTrade — Purveyors of Luxury Lifestyle Accoutrements</title>
<link rel="stylesheet" href="https://fonts.googleapis.com/css2?family=Libre+Baskerville:wght@400;700&family=Poppins:wght@300;400;500&display=swap">
<style>
:root{
  --black:#0b0b0b;
  --ink:#1f1f1f;
  --page:#e6dcd8;
  --card-light:#f3efed;
  --bronze:#9b7453;
  --bronze-dark:#6d5a4c;
  --mocha:#6b5547;
  --tan:#a07b5f;
  --gold:#c49b6a;
  --star:#f2c21b;
  --white:#ffffff;
  --muted:#cfc6c1;
}
*{margin:0;padding:0;box-sizing:border-box}
html,body{width:1200px;height:3666px;overflow:hidden}
body{position:relative;background:var(--page);font-family:'Poppins',sans-serif;color:var(--ink)}
.abs{position:absolute}
.serif{font-family:'Libre Baskerville',serif}
.btn{position:absolute;display:flex;align-items:center;justify-content:center;font-size:13px;letter-spacing:.3px;text-transform:uppercase;color:var(--white)}

/* header */
.site-header{position:absolute;left:0;top:0;width:1200px;height:112px;background:var(--black)}
.brand{position:absolute;left:150px;top:42px;display:flex;align-items:center;gap:8px;color:var(--gold);font-family:'Libre Baskerville',serif;font-size:20px}
.brand-dot{width:12px;height:12px;border-radius:50%;background:var(--gold)}
.nav a{position:absolute;top:47px;font-size:12.5px;color:var(--gold);text-decoration:none}
.nav .active{color:#e2a36b}
.nav-underline{position:absolute;left:471px;top:108px;width:50px;height:3px;background:var(--gold)}

/* hero */
.hero{position:absolute;left:0;top:112px;width:1200px;height:644px;
  background:radial-gradient(ellipse at 78% 35%,#6b4a3a 0%,#3a2a26 35%,#1d1a22 70%),#221b1f}
.hero-title{position:absolute;left:157px;top:268px;font-size:58px;line-height:73px;color:var(--white);font-weight:400}
.hero-sub{position:absolute;left:161px;top:411px;font-size:18.5px;color:var(--white);letter-spacing:.6px;font-weight:300}

/* portal cards */
.portal{position:absolute;top:668px;width:423px;height:168px;border-radius:12px;text-align:center;box-shadow:0 6px 16px rgba(0,0,0,.18)}
.portal h2{margin-top:24px;font-size:21px;font-weight:700}
.portal p{margin:8px auto 0;width:260px;font-size:13.5px;line-height:19px}
.portal .btn{left:118px;top:104px;width:188px;height:40px}
.consumer{left:161px;background:var(--card-light)}
.consumer .btn{background:var(--bronze-dark)}
.business{left:615px;background:var(--ink);color:var(--white)}
.business .btn{background:var(--bronze)}

/* about */
.about-title{left:161px;top:940px;font-size:28px;font-weight:700}
.about-text{left:161px;top:985px;width:310px;font-size:13.6px;line-height:19.6px}

/* split sections */
.split-text{position:absolute;color:var(--white)}
.split-text h2{font-size:35px;font-weight:700;margin-bottom:18px}
.split-text p{font-size:13.8px;line-height:19.6px;width:500px}
.rating{display:flex;align-items:center;gap:8px;margin-top:16px;font-size:13.5px}
.shop-link{display:inline-flex;align-items:center;gap:8px;margin-top:14px;font-size:13px;padding-bottom:4px;border-bottom:1.5px solid var(--white)}

/* product cards */
.product{position:absolute;top:2760px;width:340px;height:427px}
.product-overlay{position:absolute;left:36px;top:226px;width:268px;height:201px;background:rgba(15,12,10,.72);text-align:center;color:var(--white)}
.product-overlay h3{margin-top:12px;font-size:25px;font-weight:700;font-family:'Libre Baskerville',serif}
.product-overlay .rule{width:48px;height:2px;background:var(--white);margin:14px auto 10px}
.product-overlay .stars{display:flex;justify-content:center}
.product-overlay .label{font-size:13px;margin-top:2px}
.product .btn{left:75px;top:363px;width:190px;height:40px;background:var(--white);color:var(--ink)}

/* footer */
.site-footer{position:absolute;left:0;top:3349px;width:1200px;height:317px;background:var(--black);color:var(--white)}
.footer-heading{position:absolute;top:56px;font-size:17px;font-weight:500}
.contact-item{position:absolute;left:464px;display:flex;align-items:center;gap:10px;font-size:13.5px}
.contact-icon{width:27px;height:27px;border-radius:50%;background:var(--bronze);display:flex;align-items:center;justify-content:center}
.social{position:absolute;top:193px;width:14px;height:14px;border-radius:50%;border:1.6px solid var(--white)}
</style>
</head>
<body>

<header class="site-header">
  <div class="brand"><span class="brand-dot"></span>Velmora</div>
  <nav class="nav">
    <a class="active" style="left:477px">Home</a>
    <a style="left:585px">About Us</a>
    <a style="left:707px">Products</a>
    <a style="left:833px">Contact Us</a>
  </nav>
  <svg class="abs" style="left:948px;top:42px" width="26" height="26" viewBox="0 0 26 26" fill="none" stroke="#c49b6a" stroke-width="1.6">
    <path d="M4 8h16l-1.5 13H5.5z"/><path d="M8 8V6a4 4 0 0 1 8 0v2"/>
    <circle cx="21" cy="5" r="4" fill="#c49b6a" stroke="none"/>
  </svg>
  <svg class="abs" style="left:992px;top:42px" width="24" height="24" viewBox="0 0 24 24" fill="none" stroke="#c49b6a" stroke-width="1.6">
    <circle cx="12" cy="8" r="5"/><path d="M3 22c1-5 5-8 9-8s8 3 9 8"/>
  </svg>
  <div class="nav-underline"></div>
</header>

<section class="hero" role="img" aria-label="Bearded man in a dark suit exhaling smoke beneath a warm pendant lamp in a moody lounge"></section>
<h1 class="hero-title serif">Welcome To<br>VelmoraTrade</h1>
<p class="hero-sub">Purveyors of Luxury Lifestyle Accoutrements</p>
<div class="btn" style="left:161px;top:460px;width:162px;height:40px;background:var(--bronze)">Learn More</div>

<div class="portal consumer">
  <h2 class="serif">Shop As A Consumer</h2>
  <p>Browse and Purchase Directly As A Individual.</p>
  <div class="btn">Shop As A Consumer</div>
</div>
<div class="portal business">
  <h2 class="serif">Business Portal</h2>
  <p>Log In Or Apply For A B2B Account To Access Bulk Pricing.</p>
  <div class="btn">Business Portal</div>
</div>

<h2 class="abs about-title serif">About Us</h2>
<p class="abs about-text">Lorem Ipsum is simply dummy text of the printing and typesetting industry. Lorem Ipsum has been the industry's standard dummy text ever since the 1500s, when an unknown printer took a galley of type and scrambled it to make a type specimen book. It has survived not only five centuries, but also the leap into electronic typesetting, remaining essentially unchanged. It was popularised in the 1960s with the release of Lintrace sheets containing Lorem Ipsum passages, and more recently with desktop publishing software like Pagecraft Studio including versions of Lorem Ipsum.</p>
<div class="btn" style="left:161px;top:1288px;width:188px;height:40px;background:var(--bronze-dark)">Learn More</div>

<div class="abs" style="left:528px;top:940px;width:243px;height:365px;background:linear-gradient(160deg,#2e3a36 0%,#6b5420 55%,#a8521f 100%)" role="img" aria-label="Glass cruet of golden oil with cork stopper beside bowls of spices"></div>
<div class="abs" style="left:794px;top:979px;width:244px;height:366px;background:linear-gradient(170deg,#3a2a1c 0%,#6e4c2e 55%,#a98a68 100%)" role="img" aria-label="Decanters of spirits above an open box of cigars on a wooden table"></div>

<div class="abs" style="left:161px;top:1446px;width:878px;height:373px;background:linear-gradient(180deg,#4a2e22 0%,#6e5a36 35%,#2c2630 70%,#1c1b24 100%)" role="img" aria-label="Video still of an upscale cigar lounge with a lit bar and leather chairs"></div>
<svg class="abs" style="left:572px;top:1604px" width="54" height="54" viewBox="0 0 54 54">
  <circle cx="27" cy="27" r="27" fill="rgba(220,215,212,.6)"/><path d="M22 17l15 10-15 10z" fill="#6b6b6b"/>
</svg>

<!-- Fragrances -->
<div class="abs" style="left:0;top:1895px;width:600px;height:394px;background:linear-gradient(135deg,#d9d6d4 0%,#9a9390 45%,#7a2418 60%,#e8e5e3 100%)" role="img" aria-label="Hands in sheer white sleeves holding a red perfume bottle and its cap"></div>
<div class="abs" style="left:600px;top:1895px;width:600px;height:394px;background:var(--mocha)"></div>
<div class="split-text" style="left:653px;top:1947px">
  <h2 class="serif">Fragrances</h2>
  <p>it over 1920 years. Arthur Vellane, a Latin professor at Harwick College in Virginia, looked up one of the more obscure Latin words, consectetur, from a Lorem Ipsum passage, and going through the cites of the word in classical literature, discovered the undoubtable source. Lorem Ipsum comes from sections 1.10.32 and 1.10.33 of "de Finibus Bonorum et Malorum" (The Extremes of Good and Evil) by Cassian, it over 2000 years old. Arthur Vellane, a Latin professor at Harwick College in Virginia, looked up one of the more.</p>
  <div class="rating">
    <svg width="86" height="14" viewBox="0 0 86 14" fill="#f2c21b"><g id="s"><path d="M7 0l2 4.6 5 .5-3.8 3.3 1.1 5L7 10.9 2.7 13.4l1.1-5L0 5.1l5-.5z"/></g><use href="#s" x="18"/><use href="#s" x="36"/><use href="#s" x="54"/><use href="#s" x="72"/></svg>
    5 Star Rating
  </div>
  <div class="shop-link">SHOP NOW <svg width="16" height="8" viewBox="0 0 16 8" fill="none" stroke="#fff" stroke-width="1.3"><path d="M0 4h15M11 1l3.5 3L11 7"/></svg></div>
</div>

<!-- Cigar -->
<div class="abs" style="left:0;top:2289px;width:600px;height:396px;background:var(--tan)"></div>
<div class="abs" style="left:600px;top:2289px;width:600px;height:396px;background:linear-gradient(160deg,#8a6a4e 0%,#5a2c1c 40%,#3a2016 70%,#b89440 100%)" role="img" aria-label="Open wooden box of banded premium cigars"></div>
<div class="split-text" style="left:45px;top:2343px">
  <h2 class="serif">Cigar</h2>
  <p>it over 1920 years. Arthur Vellane, a Latin professor at Harwick College in Virginia, looked up one of the more obscure Latin words, consectetur, from a Lorem Ipsum passage, and going through the cites of the word in classical literature, discovered the undoubtable source. Lorem Ipsum comes from sections 1.10.32 and 1.10.33 of "de Finibus Bonorum et Malorum" (The Extremes of Good and Evil) by Cassian, it over 2000 years old. Arthur Vellane, a Latin professor at Harwick College in Virginia, looked up one of the more.</p>
  <div class="rating">
    <svg width="86" height="14" viewBox="0 0 86 14" fill="#f2c21b"><use href="#s"/><use href="#s" x="18"/><use href="#s" x="36"/><use href="#s" x="54"/><use href="#s" x="72"/></svg>
    5 Star Rating
  </div>
  <div class="shop-link">SHOP NOW <svg width="16" height="8" viewBox="0 0 16 8" fill="none" stroke="#fff" stroke-width="1.3"><path d="M0 4h15M11 1l3.5 3L11 7"/></svg></div>
</div>

<!-- Product categories -->
<div class="product" style="left:60px">
  <div class="abs" style="inset:0;background:linear-gradient(170deg,#1b1816 0%,#4a3526 45%,#1a1715 100%)" role="img" aria-label="Close-up of a smoking cigar tip"></div>
  <div class="product-overlay"><h3>Cigar Accessories</h3><div class="rule"></div>
    <div class="stars"><svg width="86" height="14" viewBox="0 0 86 14" fill="#f2c21b"><use href="#s"/><use href="#s" x="18"/><use href="#s" x="36"/><use href="#s" x="54"/><use href="#s" x="72"/></svg></div>
    <div class="label">5 Star Rating</div></div>
  <div class="btn">Shop Now</div>
</div>
<div class="product" style="left:430px">
  <div class="abs" style="inset:0;background:linear-gradient(170deg,#222 0%,#4d4440 45%,#6b4a2c 100%)" role="img" aria-label="Crystal decanter with a fragrance infuser and rising smoke"></div>
  <div class="product-overlay"><h3>Fragrances</h3><div class="rule"></div>
    <div class="stars"><svg width="86" height="14" viewBox="0 0 86 14" fill="#f2c21b"><use href="#s"/><use href="#s" x="18"/><use href="#s" x="36"/><use href="#s" x="54"/><use href="#s" x="72"/></svg></div>
    <div class="label">5 Star Rating</div></div>
  <div class="btn">Shop Now</div>
</div>
<div class="product" style="left:800px">
  <div class="abs" style="inset:0;background:linear-gradient(170deg,#2d3a36 0%,#6b5420 55%,#5a3a24 100%)" role="img" aria-label="Glass cruet of golden oil beside spices and herbs"></div>
  <div class="product-overlay"><h3>Oils</h3><div class="rule"></div>
    <div class="stars"><svg width="86" height="14" viewBox="0 0 86 14" fill="#f2c21b"><use href="#s"/><use href="#s" x="18"/><use href="#s" x="36"/><use href="#s" x="54"/><use href="#s" x="72"/></svg></div>
    <div class="label">5 Star Rating</div></div>
  <div class="btn">Shop Now</div>
</div>

<div class="btn" style="left:507px;top:3233px;width:188px;height:40px;background:var(--bronze-dark);font-weight:500">View All Products</div>

<footer class="site-footer">
  <div class="abs" style="left:218px;top:112px;display:flex;align-items:center;gap:7px;color:var(--gold);font-family:'Libre Baskerville',serif;font-size:17px"><span style="width:10px;height:10px;border-radius:50%;background:var(--gold)"></span>Velmora</div>
  <span class="social" style="left:205px"></span>
  <span class="social" style="left:249px"></span>
  <span class="social" style="left:291px"></span>

  <div class="footer-heading" style="left:464px">Contact Us</div>
  <div class="contact-item" style="top:100px"><span class="contact-icon"><svg width="13" height="13" viewBox="0 0 24 24" fill="#fff"><path d="M6.6 10.8a15 15 0 0 0 6.6 6.6l2.2-2.2a1 1 0 0 1 1-.25 11 11 0 0 0 3.6.6 1 1 0 0 1 1 1V20a1 1 0 0 1-1 1A17 17 0 0 1 3 4a1 1 0 0 1 1-1h3.5a1 1 0 0 1 1 1 11 11 0 0 0 .6 3.6 1 1 0 0 1-.25 1z"/></svg></span>+ 1 555 010 2040</div>
  <div class="contact-item" style="top:144px"><span class="contact-icon"><svg width="13" height="11" viewBox="0 0 24 18" fill="none" stroke="#fff" stroke-width="2"><rect x="1" y="1" width="22" height="16"/><path d="M1 1l11 9 11-9"/></svg></span>hello@velmoratrade.com</div>
  <div class="contact-item" style="top:189px"><span class="contact-icon"><svg width="13" height="11" viewBox="0 0 24 18" fill="none" stroke="#fff" stroke-width="2"><rect x="1" y="1" width="22" height="16"/><path d="M1 1l11 9 11-9"/></svg></span>122, Lorem ipsum dolird</div>

  <div class="footer-heading" style="left:797px">Subscribe To Our Newsletter</div>
  <div class="abs" style="left:790px;top:93px;width:249px;height:36px;border:1px solid var(--muted);color:var(--muted);font-size:13px;padding:8px 14px">E-mail</div>
  <div class="btn" style="left:864px;top:137px;width:102px;height:36px;background:var(--bronze);color:var(--ink);font-size:12.5px;font-weight:500">Subscribe</div>

  <div class="abs" style="left:161px;top:264px;width:878px;height:1px;background:#3a3a3a"></div>
  <div class="abs" style="left:0;top:282px;width:1200px;text-align:center;font-size:12px">Copyright©2025VelmoraTrade. All rights reserved.</div>
</footer>

</body>
</html>
```